Brisco Interiors

Hi, can you please make this design up for me. Brisco interiors text to front and Philippa Brisco text to back in black. Small love hearts to be black. Mobile number to front text and back mobile number and email address text to be white. Open to your input 🙂 Thanks in advance! Philippa

Industry/Entity Type

Interior Design

Colors

Designer to choose only greyscale colors for use in the design.

Requirements
Must have
• Little love hearts for dot on i

```html
<!DOCTYPE html>
<html lang="en">
<head>
<meta charset="utf-8">
<title>Brisco Interiors – Business Cards</title>
<link rel="stylesheet" href="https://fonts.googleapis.com/css2?family=Montserrat:wght@500&family=Poppins:wght@400&display=swap">
<style>
  :root {
    --canvas: #e6e6e6;
    --card: #ffffff;
    --card-shade: #f1f1f1;
    --ink: #111111;
    --heart: #000000;
    --band-dark: #050505;
    --band-mid: #1c1c1c;
    --on-band: #ffffff;
  }
  * { margin: 0; padding: 0; box-sizing: border-box; }
  html, body {
    width: 900px;
    height: 1200px;
    overflow: hidden;
    background: var(--canvas);
  }
  .sheet {
    position: relative;
    width: 900px;
    height: 1200px;
  }
  .card {
    position: absolute;
    left: 82px;
    width: 733px;
    height: 429px;
    border-radius: 22px;
    overflow: hidden;
    background: linear-gradient(160deg, var(--card) 55%, var(--card-shade) 100%);
    box-shadow: 0 6px 18px rgba(0, 0, 0, 0.18);
  }
  .card--back { top: 138px; }
  .card--front { top: 633px; }

  .card__title {
    position: absolute;
    left: 0;
    width: 100%;
    text-align: center;
    font-family: "Montserrat", sans-serif;
    font-weight: 500;
    color: var(--ink);
    line-height: 1;
    white-space: nowrap;
  }
  .card--back .card__title {
    top: 116px;
    font-size: 35px;
    letter-spacing: 3px;
  }
  .card--front .card__title {
    top: 176px;
    font-size: 39px;
    letter-spacing: 4.5px;
  }

  .heart-i {
    position: relative;
    display: inline-block;
  }
  .heart-i__heart {
    position: absolute;
    top: -0.22em;
    left: calc(50% - 0.5 * var(--ls, 0px));
    width: 0.26em;
    height: 0.24em;
    transform: translateX(-50%);
    fill: var(--heart);
  }
  .card--back .heart-i { --ls: 3px; }
  .card--front .heart-i { --ls: 4.5px; }

  .marble-band {
    position: absolute;
    left: 0;
    width: 100%;
    background: linear-gradient(115deg, var(--band-dark) 0%, var(--band-mid) 45%, var(--band-dark) 70%, var(--band-mid) 100%);
  }
  .card--back .marble-band { top: 272px; height: 157px; }
  .card--front .marble-band { top: 379px; height: 50px; }

  .contact {
    position: absolute;
    left: 0;
    width: 100%;
    text-align: center;
    font-family: "Poppins", sans-serif;
    font-weight: 400;
    color: var(--on-band);
    line-height: 1;
  }
  .card--back .contact { top: 326px; font-size: 19px; letter-spacing: 0.4px; }
  .card--back .contact span { display: block; margin-bottom: 10px; }
  .card--front .contact { top: 396px; font-size: 17px; letter-spacing: 0.3px; }
</style>
</head>
<body>
  <main class="sheet">
    <section class="card card--back" aria-label="Card back">
      <h1 class="card__title" aria-label="Philippa Brisco">PH<span class="heart-i">I<svg class="heart-i__heart" viewBox="0 0 24 22" aria-hidden="true"><path d="M12 21.5 10.5 20.1C5 15.2 1.5 12 1.5 7.9 1.5 4.6 4.1 2 7.4 2 9.3 2 11 2.9 12 4.3 13 2.9 14.7 2 16.6 2 19.9 2 22.5 4.6 22.5 7.9 22.5 12 19 15.2 13.5 20.1Z"/></svg></span>L<span class="heart-i">I<svg class="heart-i__heart" viewBox="0 0 24 22" aria-hidden="true"><path d="M12 21.5 10.5 20.1C5 15.2 1.5 12 1.5 7.9 1.5 4.6 4.1 2 7.4 2 9.3 2 11 2.9 12 4.3 13 2.9 14.7 2 16.6 2 19.9 2 22.5 4.6 22.5 7.9 22.5 12 19 15.2 13.5 20.1Z"/></svg></span>PPA BR<span class="heart-i">I<svg class="heart-i__heart" viewBox="0 0 24 22" aria-hidden="true"><path d="M12 21.5 10.5 20.1C5 15.2 1.5 12 1.5 7.9 1.5 4.6 4.1 2 7.4 2 9.3 2 11 2.9 12 4.3 13 2.9 14.7 2 16.6 2 19.9 2 22.5 4.6 22.5 7.9 22.5 12 19 15.2 13.5 20.1Z"/></svg></span>SCO</h1>
      <div class="marble-band" role="img" aria-label="Black marble texture with gold veining"></div>
      <p class="contact">
        <span class="contact__phone">0412 578 630</span>
        <span class="contact__email">hello@briscostudio.com.au</span>
      </p>
    </section>

    <section class="card card--front" aria-label="Card front">
      <h2 class="card__title" aria-label="Brisco Interiors">BR<span class="heart-i">I<svg class="heart-i__heart" viewBox="0 0 24 22" aria-hidden="true"><path d="M12 21.5 10.5 20.1C5 15.2 1.5 12 1.5 7.9 1.5 4.6 4.1 2 7.4 2 9.3 2 11 2.9 12 4.3 13 2.9 14.7 2 16.6 2 19.9 2 22.5 4.6 22.5 7.9 22.5 12 19 15.2 13.5 20.1Z"/></svg></span>SCO <span class="heart-i">I<svg class="heart-i__heart" viewBox="0 0 24 22" aria-hidden="true"><path d="M12 21.5 10.5 20.1C5 15.2 1.5 12 1.5 7.9 1.5 4.6 4.1 2 7.4 2 9.3 2 11 2.9 12 4.3 13 2.9 14.7 2 16.6 2 19.9 2 22.5 4.6 22.5 7.9 22.5 12 19 15.2 13.5 20.1Z"/></svg></span>NTER<span class="heart-i">I<svg class="heart-i__heart" viewBox="0 0 24 22" aria-hidden="true"><path d="M12 21.5 10.5 20.1C5 15.2 1.5 12 1.5 7.9 1.5 4.6 4.1 2 7.4 2 9.3 2 11 2.9 12 4.3 13 2.9 14.7 2 16.6 2 19.9 2 22.5 4.6 22.5 7.9 22.5 12 19 15.2 13.5 20.1Z"/></svg></span>ORS</h2>
      <div class="marble-band" role="img" aria-label="Black marble texture with gold veining"></div>
      <p class="contact">MOBILE : 0412 578 630</p>
    </section>
  </main>
</body>
</html>
```